Industrial Professional Business Card Design (Vantrel Systems)

Would like professional looking business cards. Not too busy leaning towards minimal. Should have a slogan like:
"Industrial Automation and Control".

We are a tech company that programs industrial PLC computers. We also develop custom hardware solutions. Please use the logo for inspiration.

Target Market(s)

Mining, industrial, processing, automation, factory

Industry/Entity Type

Engineering

Contact Information for Business Card

Name, phone, email, website. job title.

Font styles to use
Other font styles liked:
• droid sans

Requirements
Must have
• Use colours that go well with the logo. Not too busy design.

```html
<!DOCTYPE html>
<html lang="en">
<head>
<meta charset="utf-8">
<title>Vantrel Systems – Business Card</title>
<link rel="stylesheet" href="https://fonts.googleapis.com/css2?family=Roboto:wght@400;500;700&display=swap">
<style>
  :root {
    --backdrop: #cbcbcb;
    --navy: #1f4a70;
    --orange: #f2691e;
    --white: #ffffff;
    --card-w: 786px;
    --card-h: 447px;
    --radius: 24px;
  }
  * { margin: 0; padding: 0; box-sizing: border-box; }
  html, body {
    width: 1200px; height: 1200px; overflow: hidden;
    background: var(--backdrop);
    font-family: "Roboto", sans-serif;
  }
  .card {
    position: absolute; left: 204px;
    width: var(--card-w); height: var(--card-h);
    border-radius: var(--radius); overflow: hidden;
  }
  .card-front { top: 134px; background: var(--white); }
  .card-back { top: 622px; background: var(--navy); }
  .front-curves { position: absolute; inset: 0; }

  .brand-mark {
    position: absolute; border-radius: 50%; background: var(--orange);
  }
  .front-mark { left: 124px; top: 46px; width: 108px; height: 108px; }
  .front-brand {
    position: absolute; left: 46px; top: 168px;
    font-size: 48px; font-weight: 400; color: var(--navy); white-space: nowrap;
  }

  .holder-bar {
    position: absolute; left: 0; top: 367px; width: 13px; height: 46px;
    background: var(--orange);
  }
  .holder-name {
    position: absolute; left: 43px; top: 355px;
    font-size: 34px; font-weight: 700; color: var(--orange); letter-spacing: 0.5px;
  }
  .holder-role {
    position: absolute; left: 43px; top: 397px;
    font-size: 17px; color: var(--white); letter-spacing: 0.5px;
  }

  .tagline-rule {
    position: absolute; left: 710px; top: 270px; width: 32px; height: 2px;
    background: var(--orange);
  }
  .tagline {
    position: absolute; right: 43px; top: 292px;
    font-size: 18px; color: var(--orange); white-space: nowrap;
  }
  .contact-list { position: absolute; right: 40px; top: 330px; list-style: none; }
  .contact-item {
    display: flex; justify-content: flex-end; align-items: center; gap: 16px;
    height: 31px; font-size: 18px; color: var(--white);
  }
  .contact-item .accent { color: var(--orange); }
  .contact-icon { width: 20px; height: 20px; fill: var(--orange); }

  .back-mark { left: 302px; top: 76px; width: 182px; height: 182px; }
  .back-brand {
    position: absolute; left: 0; right: 0; top: 296px; text-align: center;
    font-size: 72px; font-weight: 400; color: var(--white); white-space: nowrap;
  }
</style>
</head>
<body>
  <section class="card card-front">
    <svg class="front-curves" width="786" height="447" viewBox="0 0 786 447" aria-hidden="true">
      <path fill="var(--orange)" d="M0,318 C310,316 590,170 748,0 L786,0 L786,6 C600,190 310,330 0,327 Z"/>
      <path fill="var(--navy)" d="M0,334 C310,334 610,200 786,22 L786,447 L0,447 Z"/>
    </svg>

    <span class="brand-mark front-mark"></span>
    <div class="front-brand">Vantrel Systems</div>

    <span class="holder-bar"></span>
    <div class="holder-name">MAREK DELVIN</div>
    <div class="holder-role">FOUNDER</div>

    <span class="tagline-rule"></span>
    <div class="tagline">Industrial Automation and Control</div>
    <ul class="contact-list">
      <li class="contact-item">+81 555 018 246
        <svg class="contact-icon" viewBox="0 0 24 24"><path d="M6.6 10.8a15.1 15.1 0 0 0 6.6 6.6l2.2-2.2a1 1 0 0 1 1-.25 11.4 11.4 0 0 0 3.6.57 1 1 0 0 1 1 1V20a1 1 0 0 1-1 1A17 17 0 0 1 3 4a1 1 0 0 1 1-1h3.5a1 1 0 0 1 1 1c0 1.25.2 2.45.57 3.57a1 1 0 0 1-.25 1z"/></svg>
      </li>
      <li class="contact-item">info@vantrelsys.com
        <svg class="contact-icon" viewBox="0 0 24 24"><path d="M2 5h20v14H2z M3.5 6.5 12 13l8.5-6.5" stroke="var(--navy)" stroke-width="1.6"/></svg>
      </li>
      <li class="contact-item"><span>www.<span class="accent">vantrelsys</span>.com</span>
        <svg class="contact-icon" viewBox="0 0 24 24"><circle cx="12" cy="12" r="10"/><path d="M2 12h20M12 2c3 3 3 17 0 20M12 2c-3 3-3 17 0 20" stroke="var(--navy)" stroke-width="1.4" fill="none"/></svg>
      </li>
    </ul>
  </section>

  <section class="card card-back">
    <span class="brand-mark back-mark"></span>
    <div class="back-brand">Vantrel Systems</div>
  </section>
</body>
</html>
```